Flyer for Aluminium recycling business

We are a startup aluminium recycling business. We don’t have a logo yet. I’ve attached a flyer created by one of our sales people but it’s a bit average and we need something a bit more modern and slick. You have creative license to completely change everything - as long as the information being communicated is the same.

Target Market(s)

Hospitality, Hotels, Apartment blocks, malls etcs

Industry/Entity Type

Aluminium recycling

Requirements
Must have
• the wording
Nice to have
• you have free license on design aspect

```html
<!DOCTYPE html>
<html lang="en">
<head>
<meta charset="utf-8">
<title>Circular Reclaim – Aluminium Recycling Flyer</title>
<link rel="stylesheet" href="https://fonts.googleapis.com/css2?family=Montserrat:wght@300;400;700;800&display=swap">
<style>
  :root{
    --page:#ffffff;
    --navy-deep:#1c2a44;
    --navy-mid:#34466a;
    --navy-light:#4a5c80;
    --green:#33cc33;
    --white:#ffffff;
  }
  *{margin:0;padding:0;box-sizing:border-box}
  html,body{width:1200px;height:1200px;overflow:hidden;background:var(--page)}
  body{font-family:'Montserrat',Arial,sans-serif;position:relative}
  .flyer{position:absolute;left:209px;top:47px;width:788px;height:1114px;overflow:hidden}
  .scrap-backdrop{position:absolute;inset:0;
    background:radial-gradient(ellipse at 70% 30%,var(--navy-light) 0%,var(--navy-mid) 40%,var(--navy-deep) 100%)}
  .abs{position:absolute;white-space:nowrap}
  .brand{left:16px;top:52px;display:flex;align-items:center;gap:26px}
  .brand-dot{width:120px;height:120px;border:8px solid var(--green);border-radius:50%}
  .brand-name{color:var(--green);font-weight:800;font-size:64px;line-height:68px;letter-spacing:1px}
  .path-line{position:absolute;left:0;top:0;overflow:visible}
  .tagline{left:0;width:788px;top:206px;text-align:center;color:var(--white);font-weight:700;font-size:21px}
  .promise{left:0;width:788px;top:248px;text-align:center;color:var(--green);font-weight:700;font-size:21px;line-height:29px}
  .section-label{background:var(--green);color:var(--white);font-weight:800;font-size:25px;height:37px;line-height:37px}
  .label-simple{left:94px;top:330px;width:228px;padding-left:37px}
  .label-examples{left:54px;top:812px;width:564px;padding-left:40px}
  .steps,.accepted{list-style:none;color:var(--white);font-weight:400;font-size:17px;line-height:23.2px}
  .steps{left:132px;top:375px}
  .accepted{left:89px;top:872px}
  .steps li,.accepted li{position:relative}
  .steps li.dot::before,.accepted li.dot::before{content:"•";position:absolute;left:-37px;font-size:9px}
  .accepted li.dot::before{left:-36px}
  .process-band{position:absolute;left:0;top:557px;width:788px;height:237px;background:var(--green)}
  .phone{left:50px;top:1028px;color:var(--green);font-weight:800;font-size:46px;letter-spacing:-1px}
  .email{right:33px;top:1048px;color:var(--green);font-weight:300;font-size:17px}
</style>
</head>
<body>
<div class="flyer">
  <div class="scrap-backdrop" role="img" aria-label="Close-up photo of shredded aluminium scrap, in navy blue tones"></div>

  <div class="abs brand">
    <div class="brand-dot"></div>
    <div class="brand-name">CIRCULAR<br>RECLAIM</div>
  </div>

  <p class="abs tagline">Playing the fair aluminium recycling game for good</p>
  <p class="abs promise">Our partnership with you is based on common sense,<br>mutual gain and a better tomorrow</p>

  <div class="abs section-label label-simple">IT'S SIMPLE:</div>
  <ul class="abs steps">
    <li class="dot">We bring you a free bin</li>
    <li class="dot">You throw all and any aluminium waste into the bin - no need to super-<br>clean it. Try to compact/squash the aluminium as much as possible</li>
    <li class="dot">We collect the bin at no charge</li>
    <li class="dot">We turn the aluminium waste into a desirable resource</li>
    <li>We pay you for however much of that resource your waste has generated -<br>and give you a report on that, so you can see how good you are</li>
  </ul>

  <div class="process-band"></div>

  <svg class="path-line" width="788" height="1114" viewBox="0 0 788 1114">
    <g fill="none" stroke="#ffffff" stroke-width="2.5" stroke-dasharray="2 3">
      <polyline points="33,184 33,633 53,633"/>
      <polyline points="732,622 757,622 757,727 732,727"/>
      <line x1="143" y1="622" x2="172" y2="622"/>
      <line x1="260" y1="622" x2="290" y2="622"/>
      <line x1="378" y1="622" x2="407" y2="622"/>
      <line x1="495" y1="622" x2="525" y2="622"/>
      <line x1="613" y1="622" x2="642" y2="622"/>
      <line x1="143" y1="727" x2="172" y2="727"/>
      <line x1="260" y1="727" x2="290" y2="727"/>
      <line x1="378" y1="727" x2="407" y2="727"/>
      <line x1="495" y1="727" x2="525" y2="727"/>
      <line x1="613" y1="727" x2="642" y2="727"/>
      <g>
        <circle cx="99" cy="622" r="44"/><circle cx="216" cy="622" r="44"/><circle cx="334" cy="622" r="44"/>
        <circle cx="451" cy="622" r="44"/><circle cx="569" cy="622" r="44"/><circle cx="686" cy="622" r="44"/>
        <circle cx="99" cy="727" r="44"/><circle cx="216" cy="727" r="44"/><circle cx="334" cy="727" r="44"/>
        <circle cx="451" cy="727" r="44"/><circle cx="569" cy="727" r="44"/><circle cx="686" cy="727" r="44"/>
      </g>
    </g>
    <g class="pin" fill="#ffffff">
      <path d="M99 587 a17 17 0 0 1 17 17 c0 12 -17 30 -17 30 s-17 -18 -17 -30 a17 17 0 0 1 17 -17z"/>
      <circle cx="99" cy="604" r="7" fill="#33cc33"/>
      <text x="99" y="648" text-anchor="middle" font-family="Montserrat, Arial, sans-serif" font-weight="800" font-size="7.5">YOU ARE HERE</text>
    </g>
    <g fill="#ffffff" opacity="0.9">
      <circle cx="216" cy="622" r="26" role="img" aria-label="Icon: bin cart"/>
      <circle cx="334" cy="622" r="26" role="img" aria-label="Icon: crushed can"/>
      <circle cx="451" cy="622" r="26" role="img" aria-label="Icon: aluminium foil roll"/>
      <circle cx="569" cy="622" r="26" role="img" aria-label="Icon: collection truck"/>
      <circle cx="686" cy="622" r="26" role="img" aria-label="Icon: sorting conveyor"/>
      <circle cx="99" cy="727" r="26" role="img" aria-label="Icon: money bag"/>
      <circle cx="216" cy="727" r="26" role="img" aria-label="Icon: ingots"/>
      <circle cx="334" cy="727" r="26" role="img" aria-label="Icon: aluminium billets"/>
      <circle cx="451" cy="727" r="26" role="img" aria-label="Icon: thermometer"/>
      <circle cx="569" cy="727" r="26" role="img" aria-label="Icon: furnace"/>
      <circle cx="686" cy="727" r="26" role="img" aria-label="Icon: smelting plant"/>
    </g>
  </svg>

  <div class="abs section-label label-examples">EXAMPLES OF WHAT WE CAN TAKE:</div>
  <ul class="abs accepted">
    <li class="dot">Used beverage cans - any</li>
    <li class="dot">Tinfoil-scrunched, crusty, burned or dirty</li>
    <li>Disposable BBQ roasting trays</li>
    <li class="dot">Aluminium takeaway containers</li>
    <li class="dot">Wine bottle screw tops (and collars - if you can get them off)</li>
    <li class="dot">Tear-off can lids</li>
  </ul>

  <p class="abs phone">020 555 0148</p>
  <p class="abs email">join@circularreclaim.co.nz</p>
</div>
</body>
</html>
```